Easter & Summer School Dance Camps

I need two flyers one for Easter camps and one for summer school
We are a performing arts and dance academy

I want a double sided flyers one side summer school one side easter camp

Please make these flyers appeal to young dancers and performers - eye catching up to date Added Tuesday, March 1, 2016

Target Market(s)

Young children and teenagers

Industry/Entity Type

School

Font styles to use
Serif
Sans Serif

Requirements
Must have
• bright colourful

```html
<!DOCTYPE html>
<html lang="en">
<head>
<meta charset="utf-8">
<title>Moonbeam Summer School</title>
<link href="https://fonts.googleapis.com/css2?family=Oswald:wght@400;600;700&family=Open+Sans:wght@400;600&display=swap" rel="stylesheet">
<style>
  :root {
    --pink: #e0357f;
    --pink-dark: #b81f63;
    --pink-soft: #f28bb8;
    --charcoal: #3a3a3d;
    --charcoal-deep: #2b2b2e;
    --grey-light: #e6e6e8;
    --white: #ffffff;
    --stage: #d9d9dc;
  }
  * { margin: 0; padding: 0; box-sizing: border-box; }
  html, body { width: 826px; height: 1200px; overflow: hidden; background: var(--stage); }
  .flyer {
    position: relative; width: 826px; height: 1200px; overflow: hidden;
    background: var(--white); font-family: "Open Sans", sans-serif;
  }
  .backdrop { position: absolute; inset: 0; }
  .photo { position: absolute; }
  .photo-dancer-leap {
    left: 430px; top: 40px; width: 380px; height: 400px;
    background: radial-gradient(ellipse at 55% 45%, #f4c9b0 0%, #e8a88a 30%, rgba(230,230,232,0) 70%);
  }
  .photo-dancer-circle {
    left: 92px; top: 292px; width: 200px; height: 200px; border-radius: 50%;
    border: 6px solid var(--white);
    background: radial-gradient(circle at 50% 45%, #d8d8da 0%, #9a9a9e 60%, #6b6b70 100%);
    box-shadow: 0 4px 14px rgba(0,0,0,.25);
  }
  .photo-boy {
    left: 40px; top: 760px; width: 300px; height: 380px;
    background: linear-gradient(180deg, rgba(255,255,255,0) 0%, #f1e4da 25%, #e9e9ec 60%, #c9c9cd 100%);
    border-radius: 40% 40% 10% 10%;
  }
  .title { position: absolute; left: 68px; top: 68px; font-family: "Oswald", sans-serif; text-transform: uppercase; }
  .title-name { display: block; font-size: 68px; font-weight: 700; color: var(--pink); line-height: 1; letter-spacing: 1px; }
  .title-sub { display: block; font-size: 36px; font-weight: 400; color: var(--charcoal); line-height: 1.2; margin-top: 4px; }
  .title-rule { position: absolute; left: 0; top: 196px; width: 330px; height: 12px; background: var(--pink); }
  .tagline { position: absolute; left: 70px; top: 510px; width: 245px; text-align: center;
    font-family: "Oswald", sans-serif; text-transform: uppercase; line-height: 1.1; }
  .tagline-lead { display: block; font-size: 34px; font-weight: 700; color: var(--pink); }
  .tagline-rest { display: block; font-size: 24px; font-weight: 600; color: var(--charcoal); }
  .brand { position: absolute; left: 66px; top: 608px; display: flex; align-items: center; gap: 10px; }
  .brand-dot { width: 20px; height: 20px; border-radius: 50%; background: var(--pink); }
  .brand-name { font-family: "Oswald", sans-serif; font-size: 42px; font-weight: 600; color: var(--pink); }
  .brand-caption { position: absolute; left: 68px; top: 668px; font-size: 11px; color: var(--charcoal); letter-spacing: 2px; text-transform: uppercase; }
  .dates { position: absolute; left: 370px; top: 700px; width: 420px; text-align: center;
    font-family: "Oswald", sans-serif; font-size: 40px; font-weight: 700; text-transform: uppercase; }
  .dates-start { color: var(--pink); }
  .dates-end { color: var(--charcoal); }
  .details { position: absolute; left: 390px; top: 790px; width: 390px; text-align: center;
    color: var(--white); font-size: 15px; line-height: 1.5; }
  .details p + p { margin-top: 14px; }
  .footer { position: absolute; left: 330px; top: 1112px; width: 496px; height: 50px;
    background: var(--pink); display: flex; align-items: center; justify-content: center;
    color: var(--white); font-size: 18px; font-weight: 600; letter-spacing: 3px; }
</style>
</head>
<body>
<main class="flyer">
  <svg class="backdrop" width="826" height="1200" viewBox="0 0 826 1200" aria-hidden="true">
    <polygon points="470,0 826,0 826,470 560,470" fill="var(--grey-light)"/>
    <polygon points="0,250 70,230 70,560 0,600" fill="var(--pink)"/>
    <polygon points="0,560 70,545 70,590 0,620" fill="var(--pink-soft)"/>
    <polygon points="0,770 826,740 826,1200 0,1200" fill="var(--charcoal)"/>
    <polygon points="0,770 330,760 330,1200 0,1200" fill="var(--charcoal-deep)"/>
    <polygon points="330,760 826,740 826,770 330,780" fill="var(--pink)"/>
    <polygon points="0,1120 330,1060 330,1200 0,1200" fill="var(--pink-dark)"/>
  </svg>

  <div class="photo photo-dancer-leap" role="img" aria-label="Photo of a dancer in white leaping mid-air with red hair flying"></div>

  <h1 class="title">
    <span class="title-name">Moonbeam</span>
    <span class="title-sub">Summer School</span>
  </h1>
  <div class="title-rule"></div>

  <div class="photo photo-dancer-circle" role="img" aria-label="Round photo of a young dancer in black mid-jump"></div>

  <p class="tagline">
    <span class="tagline-lead">A Magical</span>
    <span class="tagline-rest">West End Wiz</span>
  </p>

  <div class="brand">
    <span class="brand-dot"></span>
    <span class="brand-name">moonbeam</span>
  </div>
  <p class="brand-caption">performing arts academy</p>

  <div class="photo photo-boy" role="img" aria-label="Photo of a smiling boy in white dancing with arms outstretched"></div>

  <p class="dates"><span class="dates-start">8 August –</span> <span class="dates-end">12 August 2016</span></p>

  <section class="details">
    <p>Summer school is designed for young people who enjoy performing. The course introduces you to various disciplines of theatre: Acting, Singing and Dance.</p>
    <p>Everyone is able to develop at their own pace, no-one is forced to perform and there are opportunities for you to explore performance techniques.</p>
    <p>Students will develop key skills in teamwork, communication and confidence whilst building friendships and having fun!</p>
    <p>The week ends with a showing, to friends and family, of the skills and musical numbers achieved during the course</p>
  </section>

  <footer class="footer">Visit us at: www.moonbeamdanceacademy.co.uk</footer>
</main>
</body>
</html>
```